Book cover design for a collection of poetry - The Lanternfield

Book cover and back design need to be moody, nostalgic, reflective, ethereal. Melancholy and other worldly. Cover design should not be time specific to a period or place but if applicable should reflect British landscape. Book cover should be in tones of blue and must include the title and author (THE LANTERNFIELD BY DORIAN WELKBRIDGE). We love the idea of rain, and looking out of a window. See attached designs. A world you are observing but not in.

Industry/Entity Type

Book Publisher

Font styles to use
Serif
Script

Colors
3176b5
3377b5
85acd3
eaf1f7
0792cd
33a6d7
86cae7
ecf7fb
86cfc6

Requirements
Must have
• The colour blue in it, must be melancholy and reflective.
Nice to have
• Rain in the cover.
Should not have
• Any bright colours.

```html
<!DOCTYPE html>
<html lang="en">
<head>
<meta charset="utf-8">
<title>The Lanternfield — Dorian Welkbridge</title>
<link href="https://fonts.googleapis.com/css2?family=Marcellus+SC&family=Barlow+Semi+Condensed:wght@400;500&display=swap" rel="stylesheet">
<style>
  :root {
    --ink-deep: #050d16;
    --night: #0a1824;
    --storm: #122b3e;
    --rain-blue: #1d4460;
    --pane-light: #7fa9c9;
    --pane-mid: #3e6a8a;
    --pane-dark: #101d24;
    --text: #f4f7fa;
    --seam: rgba(150, 170, 190, 0.35);
  }
  * { margin: 0; padding: 0; box-sizing: border-box; }
  html, body {
    width: 1200px; height: 873px; overflow: hidden;
    background: var(--ink-deep);
  }
  .cover-wrap {
    position: relative; width: 1200px; height: 873px; overflow: hidden;
    background: var(--ink-deep);
    color: var(--text);
  }

  /* Back cover */
  .back-cover {
    position: absolute; left: 0; top: 0; width: 546px; height: 873px;
  }
  .back-cover__rain {
    position: absolute; inset: 0;
    background:
      radial-gradient(ellipse 60% 70% at 35% 40%, rgba(40, 84, 112, 0.55), transparent 70%),
      linear-gradient(90deg, var(--storm) 0%, var(--rain-blue) 30%, var(--storm) 60%, var(--night) 100%);
  }
  .back-cover__blurb {
    position: absolute; left: 82px; top: 248px; width: 382px;
    font-family: "Barlow Semi Condensed", sans-serif;
    font-weight: 500; font-size: 13.4px; line-height: 27.3px;
    letter-spacing: 0.6px; text-transform: uppercase; text-align: center;
  }
  .back-cover__blurb p + p { margin-top: 27px; }

  /* Spine */
  .spine {
    position: absolute; left: 546px; top: 0; width: 110px; height: 873px;
    background: linear-gradient(180deg, var(--night), #08131d);
    border-left: 1px solid var(--seam);
    border-right: 1px solid var(--seam);
  }
  .spine__author {
    position: absolute; top: 106px; width: 100%; text-align: center;
    font-family: "Barlow Semi Condensed", sans-serif;
    font-weight: 500; font-size: 18px; line-height: 29px; letter-spacing: 1px;
  }
  .spine__title {
    position: absolute; left: 50%; top: 266px;
    transform-origin: 0 0; transform: rotate(90deg) translateY(-50%);
    white-space: nowrap;
    font-family: "Marcellus SC", serif; font-size: 34px; letter-spacing: 1px;
  }

  /* Front cover */
  .front-cover {
    position: absolute; left: 656px; top: 0; width: 544px; height: 873px;
    background: radial-gradient(ellipse 80% 60% at 55% 35%, #0d1d2b, var(--ink-deep) 75%);
  }
  .front-cover__window {
    position: absolute; left: 61px; top: 69px; width: 426px; height: 514px;
    background:
      linear-gradient(180deg, transparent 0%, transparent 100%),
      linear-gradient(180deg, var(--pane-light) 0%, var(--pane-mid) 45%, #2b4a56 68%, var(--pane-dark) 100%);
    box-shadow: inset 0 0 0 34px rgba(70, 55, 40, 0.55), 0 0 30px rgba(0,0,0,0.6);
  }
  .front-cover__title {
    position: absolute; left: 0; top: 632px; width: 100%; text-align: center;
    font-family: "Marcellus SC", serif; font-size: 40px; line-height: 66px;
    letter-spacing: 0.5px;
  }
  .front-cover__author {
    position: absolute; left: 0; top: 760px; width: 100%; text-align: center;
    font-family: "Barlow Semi Condensed", sans-serif;
    font-weight: 400; font-size: 22px; letter-spacing: 3.4px;
  }
</style>
</head>
<body>
<main class="cover-wrap">
  <section class="back-cover">
    <div class="back-cover__rain" role="img" aria-label="Rain droplets running down a dark blue window pane"></div>
    <div class="back-cover__blurb">
      <p>The Lanternfield is a collection of poetry.</p>
      <p>Told in two parts we first meet Charles — aged, crippled and left alone in his inherited marsh house - reflecting on his life and his marriage to beautiful Alice who we meet in part two. Alice is suicidal, manically depressed and struggling with life as a wife and mother. She meets, harbors and falls in love with a soldier during WWII and her world is changed forever.</p>
      <p>Moving through the 20th century, this life and the next, The Lanternfield interweaves grief, loss, the after-life, mental illness, and ultimately the true nature of love.</p>
    </div>
  </section>

  <section class="spine">
    <div class="spine__author">Dorian<br>Welkbridge</div>
    <div class="spine__title">The Lanternfield</div>
  </section>

  <section class="front-cover">
    <div class="front-cover__window" role="img" aria-label="Old wooden-framed window with rain-streaked panes, a lightning storm over dark hills beyond"></div>
    <h1 class="front-cover__title">The<br>Lanternfield</h1>
    <div class="front-cover__author">Dorian Welkbridge</div>
  </section>
</main>
</body>
</html>
```